Web Design Project

We need a design for the actual web.
http://mirela.vunto.example/
It will be a cakes and cupcakes online shop.

It is a one page site, with five anchors.

Inicio (Home)
Here it will show a brief explanation about our shop, just explaining we sell really nice cakes and cupcakes. Also we want to show a slide gallery, like the one it is working, but with not nice choosen pictures.

Productos/Tortas
This two anchors will be just one at the end, but I wanted to show the two options for accessing the different products, tabs or buttons. You can click on the firsts images on that links for see the "pop up image" with a better explanation of every product.

Contacto
Here it will show a little form, that will only appear in smartphones and maybe tablets, this form needs to be similar and much more simple than the principal form (the next anchor), so just focus on it once the next one its done.

Form
This will be the way the users will send the orders, its a complex form, focused on the UX. We dont want the user to type too much and we want it to surprise the user and fell really comfortable.

Industry/Entity Type

Tv

Requirements
Must have

• -Must have side menu, but you can redesign it completelly, but with the same structure
-Its important to focus all the content in the top and middle, we arent sure about users screens and it we set info at the footer, maybe its not gonna show (no scroll vertical).
-You can change all the colours of the site, we are open to new visions, you can surprise us.

```html
<!DOCTYPE html>
<html lang="es">
<head>
<meta charset="utf-8">
<title>Mirela Bakes — Tortas</title>
<link href="https://fonts.googleapis.com/css2?family=Norican&family=Crimson+Text:wght@400&display=swap" rel="stylesheet">
<style>
:root{
  --cream:#f4f2ea;
  --teal:#2a9a98;
  --olive:#857544;
  --olive-light:#8f7f4d;
  --tab-bg:rgba(232,226,200,.78);
  --tab-ink:#9a8236;
  --card:#f8eba0;
  --card-ink:#8a6f1c;
  --heading-ink:#7d6414;
  --close-ink:#a09a82;
  --photo-light:#f1e6c8;
  --photo-warm:#d9bf8a;
  --footer:#b08810;
  --white:#ffffff;
}
*{box-sizing:border-box;margin:0;padding:0}
html,body{width:1200px;height:962px;overflow:hidden}
body{position:relative;background:linear-gradient(135deg,var(--olive-light),var(--olive));font-family:"Crimson Text",serif}
.script{font-family:"Norican",cursive}

.site-header{position:absolute;left:0;top:0;width:1200px;height:144px;background:var(--cream)}
.site-header::after{content:"";position:absolute;left:0;top:144px;width:1200px;height:10px;
  background:radial-gradient(circle at 8px 0,var(--cream) 8px,transparent 8.5px) 0 0/16px 10px repeat-x}
.brand{position:absolute;left:139px;top:28px;width:130px;font-family:"Crimson Text",serif;font-size:34px;line-height:34px;color:var(--teal);display:flex;align-items:center;gap:8px}
.brand-mark{width:14px;height:14px;border-radius:50%;background:var(--teal);flex:none}
.contact{position:absolute;left:737px;top:27px;display:flex;align-items:center;gap:10px;color:var(--teal);font-size:20px}
.contact svg{width:28px;height:28px}
.social{position:absolute;top:26px;width:29px;height:29px;border-radius:4px;background:var(--teal)}
.social.one{left:991px}.social.two{left:1025px}
.main-nav{position:absolute;top:77px;left:0;width:1200px;height:44px}
.main-nav a{position:absolute;top:0;height:44px;line-height:46px;font-size:32px;color:var(--teal);text-decoration:none}
.main-nav a.active{background:var(--teal);color:var(--white);border-radius:5px;padding:0 14px}

.product-tabs a{position:absolute;top:185px;width:200px;height:48px;border-radius:6px;background:var(--tab-bg);color:var(--tab-ink);font-size:30px;line-height:52px;text-align:center;text-decoration:none}

.product-modal{position:absolute;left:145px;top:263px;width:906px;height:498px;background:var(--card);border-radius:8px;box-shadow:6px 10px 14px rgba(60,45,10,.35)}
.product-photo{position:absolute;left:44px;top:26px;width:206px;height:128px;border-radius:6px;background:linear-gradient(160deg,var(--photo-light),var(--photo-warm))}
.product-name{position:absolute;left:0;width:316px;top:164px;text-align:center;font-size:29px;line-height:36px;color:var(--card-ink)}
.modal-body{position:absolute;left:314px;top:8px;width:566px;color:var(--card-ink)}
.modal-body h1{font-weight:400;font-size:52px;line-height:64px;color:var(--heading-ink)}
.modal-body p{font-size:22.5px;line-height:25px;margin-bottom:25px}
.modal-body p:first-of-type{margin-top:6px}
.close{position:absolute;left:858px;top:17px;width:28px;height:30px}

.site-footer{position:absolute;left:0;top:775px;width:1200px;height:187px;background:var(--footer)}
.site-footer::before{content:"";position:absolute;left:0;top:-6px;width:1200px;height:6px;
  background:radial-gradient(circle at 5px 6px,var(--footer) 5px,transparent 5.5px) 0 0/10px 6px repeat-x}
.site-footer p{position:absolute;left:0;top:32px;width:1200px;text-align:center;white-space:nowrap;color:var(--white);font-size:30px;line-height:41px}
</style>
</head>
<body>
<header class="site-header">
  <div class="brand"><span class="brand-mark"></span>Mirela Bakes</div>
  <div class="contact">
    <svg viewBox="0 0 24 24" aria-hidden="true"><path fill="currentColor" d="M6.6 10.8a15 15 0 0 0 6.6 6.6l2.2-2.2a1 1 0 0 1 1-.25 11.4 11.4 0 0 0 3.6.57 1 1 0 0 1 1 1V20a1 1 0 0 1-1 1A17 17 0 0 1 3 4a1 1 0 0 1 1-1h3.5a1 1 0 0 1 1 1c0 1.25.2 2.45.57 3.57a1 1 0 0 1-.25 1z"/></svg>
    <span>Call us: ( 2938 ) 5550 142</span>
  </div>
  <span class="social one" role="img" aria-label="Red social"></span>
  <span class="social two" role="img" aria-label="Red social"></span>
  <nav class="main-nav script">
    <a href="#inicio" style="left:506px">Inicio</a>
    <a href="#productos" style="left:610px">Productos</a>
    <a href="#tortas" class="active" style="left:742px">Tortas</a>
    <a href="#contacto" style="left:862px">Contacto</a>
    <a href="#form" style="left:988px">Form</a>
  </nav>
</header>

<nav class="product-tabs script">
  <a href="#cupcakes" style="left:293px">Cupcakes</a>
  <a href="#tortas" style="left:505px">Tortas</a>
  <a href="#eventos" style="left:717px">Eventos</a>
</nav>

<section class="product-modal">
  <div class="product-photo" role="img" aria-label="Foto del cheesecake con frutillas"></div>
  <div class="product-name">Cheesecake</div>
  <div class="modal-body">
    <h1>Ingredientes</h1>
    <p>Your couch. I it's mine.</p>
    <p>Im a cool paragraph that lives inside of an even cooler modal. Wins</p>
    <p>I am so happy, my dear friend, so absorbed in the exquisite sense of mere tranquil existence, that I neglect my talents. I should be incapable of drawing a single stroke at the present moment; and yet I feel that I never was a greater artist than now.</p>
    <p>When, while the lovely valley teems with vapour around me, and the meridian sun strikes the upper surface of the impenetrable foliage of my trees, and but a few stray gleams steal into the inner sanctuary...</p>
  </div>
  <svg class="close" viewBox="0 0 28 30" aria-label="Cerrar"><path d="M3 3 L25 27 M25 3 L3 27" stroke="var(--close-ink)" stroke-width="7" stroke-linecap="square"/></svg>
</section>

<footer class="site-footer">
  <p class="script">Lorem ipsum dolor sit amet consectetur adipiscing elit. Cras dignissim ultricies<br>nunc et porttitor. Quisque magna turpis, pharetra eu iaculis et, porttitor id quam.<br>In hac habitasse platea dictumst.</p>
</footer>
</body>
</html>
```